Lumora Dwellings

Design a stylish Business card- we would like a businness card design that suits plastic business cards. Our card needs to show that we are tech savy and technology based so the design is crucial.

Target Market(s)

22-40

Industry/Entity Type

Plastic

Requirements
Must have
• attached is our logo. also double sided card would be nice.
my details

Tobias Fenwright
Director
0471596234
www.lumoradwellings.com.au
17 Ashcombe Lane, West Perth

```html
<!DOCTYPE html>
<html lang="en">
<head>
<meta charset="utf-8">
<title>Lumora Dwellings – Business Card</title>
<link rel="stylesheet" href="https://fonts.googleapis.com/css2?family=Source+Sans+3:wght@400;600;700&display=swap">
<style>
  :root {
    --bg: #d9d6d2;
    --card: #050505;
    --blue: #29aee0;
    --blue-deep: #0a7fb0;
    --silver: #b9bcbf;
    --text: #e6e6e6;
    --muted: #c9c9c9;
  }
  * { margin: 0; padding: 0; box-sizing: border-box; }
  html, body { width: 1200px; height: 463px; overflow: hidden; }
  body {
    background: var(--bg);
    font-family: "Source Sans 3", Arial, sans-serif;
    position: relative;
  }
  .card {
    position: absolute;
    top: 97px;
    width: 466px;
    height: 268px;
    background: var(--card);
    overflow: hidden;
    box-shadow: 0 4px 10px rgba(0,0,0,0.35);
    color: var(--text);
  }
  .card--front { left: 97px; }
  .card--back { left: 638px; }
  .swoosh { position: absolute; left: 0; top: 0; width: 466px; height: 268px; }
  .brand {
    position: absolute;
    left: 0; right: 0; top: 50px;
    display: flex;
    justify-content: center;
    align-items: center;
    gap: 12px;
  }
  .brand__mark {
    width: 44px; height: 44px;
    background: var(--silver);
    border-radius: 6px;
  }
  .brand__lockup { display: flex; flex-direction: column; }
  .brand__tagline {
    font-size: 12px;
    font-weight: 400;
    color: var(--text);
    margin-bottom: 3px;
    text-align: right;
  }
  .brand__name {
    font-size: 30px;
    font-weight: 700;
    line-height: 1;
    letter-spacing: 0.5px;
    color: var(--blue);
    text-transform: uppercase;
  }
  .contact {
    position: absolute;
    left: 0; right: 0;
    text-align: center;
    font-size: 12px;
    color: var(--muted);
  }
  .contact--address { top: 154px; }
  .contact--lines {
    top: 180px;
    display: flex; justify-content: center; gap: 10px; align-items: center;
  }
  .contact__item { display: inline-flex; align-items: center; gap: 4px; }
  .contact__icon { width: 10px; height: 10px; }
  .person {
    position: absolute;
    left: 0; right: 0; top: 208px;
    text-align: center;
  }
  .person__name { font-size: 15px; font-weight: 700; color: var(--text); line-height: 1.1; }
  .person__role { font-size: 12px; color: var(--muted); }
  .back-web {
    position: absolute;
    left: 0; right: 0; top: 215px;
    text-align: center;
    font-size: 12px;
    color: var(--muted);
  }
</style>
</head>
<body>

<section class="card card--front">
  <svg class="swoosh" viewBox="0 0 466 268" aria-hidden="true">
    <defs>
      <linearGradient id="blueFront" x1="0" y1="0" x2="1" y2="0">
        <stop offset="0" stop-color="#1fb4ea"/>
        <stop offset="1" stop-color="#0a7fb0"/>
      </linearGradient>
    </defs>
    <path d="M0,192 C80,238 220,262 466,202 L466,268 L0,268 Z" fill="url(#blueFront)"/>
    <path d="M150,268 C290,256 390,236 466,212 L466,222 C390,248 300,264 235,268 Z" fill="#050505"/>
    <path d="M160,252 C300,246 400,222 466,192" fill="none" stroke="#b9bcbf" stroke-width="3"/>
  </svg>

  <div class="brand">
    <span class="brand__mark"></span>
    <div class="brand__lockup">
      <span class="brand__tagline">Smarter Living Starts With A Tap</span>
      <span class="brand__name">Lumora Dwellings</span>
    </div>
  </div>

  <p class="contact contact--address">17 Ashcombe Lane, West Perth</p>
  <p class="contact contact--lines">
    <span class="contact__item">
      <svg class="contact__icon" viewBox="0 0 10 10" aria-hidden="true"><path d="M2,1 L4,1 L4.5,3 L3.3,4 C4,5.5 4.5,6 6,6.7 L7,5.5 L9,6 L9,8 C5,8.5 1.5,5 2,1 Z" fill="#c9c9c9"/></svg>
      0471596234
    </span>
    <span class="contact__item">
      <svg class="contact__icon" viewBox="0 0 10 10" aria-hidden="true"><circle cx="5" cy="5" r="4" fill="none" stroke="#c9c9c9" stroke-width="1"/><path d="M1,5 H9 M5,1 C3,3 3,7 5,9 M5,1 C7,3 7,7 5,9" fill="none" stroke="#c9c9c9" stroke-width="0.8"/></svg>
      www.lumoradwellings.com.au
    </span>
  </p>

  <div class="person">
    <p class="person__name">Tobias Fenwright</p>
    <p class="person__role">Director</p>
  </div>
</section>

<section class="card card--back">
  <svg class="swoosh" viewBox="0 0 466 268" aria-hidden="true">
    <defs>
      <linearGradient id="blueBack" x1="0" y1="0" x2="1" y2="0">
        <stop offset="0" stop-color="#1fb4ea"/>
        <stop offset="1" stop-color="#0a7fb0"/>
      </linearGradient>
    </defs>
    <path d="M0,192 C80,238 220,262 466,202 L466,268 L0,268 Z" fill="url(#blueBack)"/>
    <path d="M150,268 C290,256 390,236 466,212 L466,222 C390,248 300,264 235,268 Z" fill="#050505"/>
    <path d="M160,252 C300,246 400,222 466,192" fill="none" stroke="#b9bcbf" stroke-width="3"/>
  </svg>

  <div class="brand">
    <span class="brand__mark"></span>
    <div class="brand__lockup">
      <span class="brand__tagline">Smarter Living Starts With A Tap</span>
      <span class="brand__name">Lumora Dwellings</span>
    </div>
  </div>

  <p class="back-web">www.lumoradwellings.com.au</p>
</section>

</body>
</html>
```